Music Artist Needs Flyer Design ASAP

Looking for a flyer design to promote for artist release party. Music artist is mainly hip hop based. We would like designs that are simple, creative and eye catching.

Requirements
Must have
• The flyer must have the photo of the artist I attached incorporated into the design. Must say "Free ZuRK" Release Party, Live at Toller's Bar Thursday Dec.27 2012 (artist name=ZuRK VeNT), show starts at 8pm, No cover charge, 21 and over, Register to Win Borvale Comets tickets Giveaway

```html
<!DOCTYPE html>
<html lang="en">
<head>
<meta charset="utf-8">
<title>"Free ZuRK" Release Party</title>
<link rel="stylesheet" href="https://fonts.googleapis.com/css2?family=Stardos+Stencil:wght@700&display=swap">
<style>
  :root {
    --ink: #1c1a08;
    --glow: #fff8a0;
    --yellow: #f3e02a;
    --amber: #e8a21c;
    --rust: #b8661a;
    --brown: #8a4a14;
    --skin: #e09a4a;
    --tee: #f4ecc0;
    --graphic: #3a3018;
  }
  html, body {
    margin: 0;
    padding: 0;
    width: 1200px;
    height: 675px;
    overflow: hidden;
    background: var(--amber);
  }
  .flyer {
    position: relative;
    width: 1200px;
    height: 675px;
    overflow: hidden;
    font-family: "Stardos Stencil", "Impact", sans-serif;
    font-weight: 700;
    color: var(--ink);
    text-transform: uppercase;
    background: linear-gradient(90deg, var(--rust) 0%, var(--amber) 20%, var(--yellow) 45%, var(--amber) 80%, var(--rust) 100%);
  }
  .banknote-backdrop {
    position: absolute;
    inset: 0;
    background:
      radial-gradient(ellipse 22% 40% at 36% 48%, rgba(255,248,160,0.9) 0%, rgba(243,224,42,0.5) 60%, rgba(243,224,42,0) 100%),
      radial-gradient(ellipse 28% 48% at 36% 50%, rgba(160,110,20,0) 70%, rgba(160,110,20,0.35) 78%, rgba(160,110,20,0) 86%),
      radial-gradient(ellipse 16% 30% at 6% 58%, rgba(138,74,20,0.6), rgba(138,74,20,0) 100%),
      radial-gradient(ellipse 18% 40% at 10% 30%, rgba(184,102,26,0.55), rgba(184,102,26,0) 100%),
      radial-gradient(ellipse 20% 40% at 88% 30%, rgba(138,74,20,0.45), rgba(138,74,20,0) 100%),
      radial-gradient(ellipse 25% 25% at 92% 95%, rgba(138,74,20,0.5), rgba(138,74,20,0) 100%),
      linear-gradient(180deg, rgba(138,74,20,0.15), rgba(138,74,20,0) 30%, rgba(138,74,20,0) 70%, rgba(138,74,20,0.25));
  }
  .artist-photo {
    position: absolute;
    left: 300px;
    top: 30px;
    width: 360px;
    height: 645px;
    border-radius: 46% 46% 30% 30% / 22% 22% 10% 10%;
    background:
      radial-gradient(ellipse 22% 14% at 42% 14%, var(--skin) 0%, rgba(224,154,74,0.7) 60%, rgba(224,154,74,0) 100%),
      radial-gradient(ellipse 30% 30% at 45% 55%, rgba(58,48,24,0.75) 0%, rgba(58,48,24,0.4) 55%, rgba(58,48,24,0) 100%),
      linear-gradient(180deg, rgba(255,248,160,0) 0%, var(--tee) 32%, #f0d680 80%, rgba(243,224,42,0.3) 100%);
    box-shadow: 0 0 60px 30px rgba(255,248,160,0.6);
  }
  .line { position: absolute; margin: 0; line-height: 1; white-space: nowrap; }
  .title { left: 90px; top: 12px; font-size: 66px; letter-spacing: 3px; }
  .venue { left: 26px; top: 80px; font-size: 34px; letter-spacing: 2px; }
  .artist-name { left: 22px; top: 132px; font-size: 21px; letter-spacing: 3px; }
  .date { left: 668px; top: 82px; font-size: 38px; letter-spacing: 3px; }
  .show-time { left: 757px; width: 400px; text-align: center; font-size: 52px; letter-spacing: 3px; }
  .show-time.first { top: 183px; }
  .show-time.second { top: 253px; }
  .age { left: 766px; top: 370px; font-size: 52px; letter-spacing: 3px; }
  .cover { left: 36px; top: 483px; font-size: 52px; letter-spacing: 3px; }
  .register { left: 206px; top: 577px; font-size: 38px; letter-spacing: 3px; }
  .giveaway { left: 760px; top: 577px; font-size: 38px; letter-spacing: 3px; }
  .team {
    position: absolute;
    left: 605px;
    top: 478px;
    width: 145px;
    text-align: center;
  }
  .team-mark {
    display: block;
    width: 96px;
    height: 96px;
    margin: 0 auto 14px;
    border-radius: 50%;
    background: var(--rust);
  }
  .team-name { font-size: 26px; line-height: 1.05; color: var(--ink); }
</style>
</head>
<body>
  <main class="flyer">
    <div class="banknote-backdrop" role="img" aria-label="Warm orange collage of banknote engravings behind the text"></div>
    <div class="artist-photo" role="img" aria-label="Photo of the artist ZuRK VeNT in a white graphic tee, glowing yellow halo"></div>

    <h1 class="line title">"Free ZuRK" Release Party</h1>
    <p class="line venue">Live at Toller's Bar</p>
    <p class="line artist-name">(Artist name=ZuRK VeNT)</p>
    <p class="line date">Thursday Dec.27 2012</p>

    <p class="line show-time first">Show starts</p>
    <p class="line show-time second">at 8pm</p>
    <p class="line age">21 and over</p>

    <p class="line cover">No cover charge</p>
    <p class="line register">Register to win</p>
    <div class="team">
      <span class="team-mark"></span>
      <span class="team-name">Borvale Comets</span>
    </div>
    <p class="line giveaway">Tickets giveaway</p>
  </main>
</body>
</html>
```